Letterhead/Envelope Design Project

We are a 501c3 non-profit that supports educational programs at Oskenna Ridge Meadows State Park in California. We have new logo and need letterhead. The design needs need incorporate the logo attached. It needs to contain the information in document attached called "information" attached. Please see our website ridgemeadows.org to get the feeling and colors we are looking for.

```html
<!DOCTYPE html>
<html lang="en">
<head>
<meta charset="utf-8">
<title>Oskenna Ridge Meadows Association – Stationery</title>
<link href="https://fonts.googleapis.com/css2?family=Open+Sans:wght@400;700&family=Roboto+Condensed:wght@400&display=swap" rel="stylesheet">
<style>
:root{
  --forest:#21502a;
  --bark:#7b4a32;
  --paper:#ffffff;
  --backdrop:#cccccc;
  --ink:#1a1a1a;
  --muted:#444;
}
*{box-sizing:border-box;margin:0;padding:0}
html,body{width:1200px;height:1000px;overflow:hidden;background:var(--backdrop)}
body{position:relative;font-family:"Open Sans",Arial,sans-serif;color:var(--ink)}
.sheet{position:absolute;background:var(--paper);box-shadow:8px 8px 10px rgba(0,0,0,.28);overflow:hidden}
.band{position:absolute;left:0;top:0;width:100%;background:var(--forest)}
.brand-mark{position:absolute;background:var(--paper);border:2px solid var(--forest);display:flex;align-items:center;justify-content:center;text-align:center;color:var(--forest);font-weight:700;text-transform:uppercase;line-height:1.15}

/* letterhead */
.letterhead{left:60px;top:138px;width:511px;height:661px}
.letterhead .band{height:35px}
.letterhead .brand-mark{left:222px;top:21px;width:68px;height:79px;font-size:8px;padding:4px}
.letter-body{position:absolute;left:54px;top:110px;width:410px;font-size:9px;line-height:17.6px}
.recipient{font-weight:700;margin-bottom:17.6px}
.letter-body p{margin-bottom:17.6px}
.signature{display:block;width:106px;height:52px;margin:-4px 0 2px;background:linear-gradient(90deg,#e8e8e8,#f6f6f6)}
.letter-footer{position:absolute;left:54px;top:626px;width:402px;border-top:2px solid var(--bark);padding-top:7px;display:flex;justify-content:space-between;font-family:"Roboto Condensed",Arial,sans-serif;font-size:6.6px;color:var(--muted)}
.letter-footer span{display:flex;align-items:center;gap:4px;white-space:nowrap}
.letter-footer svg{width:8px;height:8px;flex:none}

/* envelopes */
.envelope-front{left:628px;top:206px;width:509px;height:231px}
.envelope-front .band{height:34px}
.envelope-front .brand-mark{left:20px;top:14px;width:47px;height:54px;font-size:5.4px;padding:3px}
.return-address{position:absolute;left:20px;top:74px;font-family:"Roboto Condensed",Arial,sans-serif;font-size:6.6px;line-height:8px;color:var(--muted)}
.envelope-back{left:628px;top:488px;width:512px;height:233px}
.envelope-back svg{position:absolute;left:0;top:0}
</style>
</head>
<body>

<section class="sheet letterhead" aria-label="Letterhead">
  <div class="band"></div>
  <div class="brand-mark">Oskenna Ridge Meadows Association</div>
  <div class="letter-body">
    <div class="recipient">To<br>Lorem Ipsum is simply<br>Lorem Ipsum is Lorem Ipsum is<br>Lorem Ipsum is</div>
    <p>dummy text of the printing and typesetting industry. Lorem Ipsum has been the industry's standard dummy text ever since the 1500s, when an unknown printer took a galley of type and scrambled it to make a type specimen book. It has survived not only five centuries, but also the leap into electronic typesetting, remaining essentially unchanged.</p>
    <p>It is a long established fact that a reader will be distracted by the readable content of a page when looking at its layout. The point of using Lorem Ipsum is that it has a more-or-less normal distribution of letters, as opposed to using 'Content here, content here', making it look like readable English. Many desktop publishing packages and web page editors now use Lorem Ipsum as their default model text, and a search for 'lorem .</p>
    <p>Contrary to popular belief, Lorem Ipsum is not simply random text. It has roots in a piece of classical Latin literature from 45 BC, making it over 2000 years old. Edwin Harlow, a Latin professor at Larkfield College in Vermont, looked up one of the more obscure Latin words, consectetur, from a Lorem Ipsum passage,</p>
    <div class="closing">Lorem Ipsum</div>
    <span class="signature" role="img" aria-label="Handwritten signature"></span>
    <div class="signer">Lorem Ipsum is a dummy</div>
  </div>
  <footer class="letter-footer">
    <span><svg viewBox="0 0 10 10"><rect x="0.5" y="2" width="9" height="7" fill="none" stroke="#21502a"/><rect x="2" y="0.5" width="6" height="2.5" fill="#21502a"/></svg>209.555.0142</span>
    <span><svg viewBox="0 0 10 10"><rect x="0.5" y="2" width="9" height="7" fill="none" stroke="#21502a"/><rect x="2.5" y="4" width="5" height="3" fill="#21502a"/></svg>209.555.0187</span>
    <span><svg viewBox="0 0 10 10"><rect x="0.5" y="0.5" width="9" height="9" fill="#21502a"/><path d="M2 3.5h6v4H2z M2 3.5l3 2.2 3-2.2" fill="none" stroke="#fff" stroke-width=".8"/></svg>info@ridgemeadows.org</span>
    <span><svg viewBox="0 0 10 10"><rect x="0.5" y="0.5" width="9" height="9" fill="#21502a"/><circle cx="5" cy="5" r="2.8" fill="none" stroke="#fff" stroke-width=".8"/><path d="M2.2 5h5.6M5 2.2v5.6" stroke="#fff" stroke-width=".6"/></svg>www.ridgemeadows.org</span>
    <span><svg viewBox="0 0 10 10"><rect x="0.5" y="0.5" width="9" height="9" fill="#21502a"/><path d="M5 8.5 2.8 5a2.3 2.3 0 1 1 4.4 0z" fill="#fff"/><circle cx="5" cy="4" r=".9" fill="#21502a"/></svg>P.O. Box 4410, Fenwick, CA 95990-4410</span>
  </footer>
</section>

<section class="sheet envelope-front" aria-label="Envelope front">
  <div class="band"></div>
  <div class="brand-mark">Oskenna Ridge Meadows Association</div>
  <div class="return-address">P.O. Box 4410, Fenwick<br>CA 95990-4410</div>
</section>

<section class="sheet envelope-back" aria-label="Envelope back">
  <svg width="512" height="233" viewBox="0 0 512 233">
    <path d="M0 0H512V4Q506 40 500 76Q256 72 12 76Q6 40 0 4Z" fill="#21502a" stroke="#173c1e" stroke-width="1"/>
  </svg>
</section>

</body>
</html>
```